Onboarding Infographic/brochure

We are a small criminal defense firm looking to create some sort of infographic or brochure that we can onboard new clients with. We are currently sending it out via email but want something a bit cooler and fun to send to clients. The information is:

A Few Quick Rules

We are here to help each step of the way. While questions are never discouraged, this letter will answer some of the most common ones we get asked.

Communications

As a client, you should always be in the loop. While we will try to respond to questions as quickly as possible, sometimes we are unable to respond right away. Do not worry - we promise to get back to you soon. Some questions might take some time to research, and a correct answer is better than a quick one.

Appointments

One of the benefits of having an attorney is the ability to discuss your case outside of court, minus the stress and headaches. If you need an appointment, please contact the office.

Appointments must be scheduled in advance. We do not want you to make a special trip to the office only to learn that we are in court or otherwise unavailable.

Jail Visits

If your family member is currently in jail, we take that very seriously. We will visit your loved one and introduce ourselves. While the case is ongoing, we ask that a family member be designated a “contact” person so that messages can be relayed quickly. Never discuss the facts of the case over the phone with someone who is in jail. Jail calls are recorded and we have seen too many cases go south based on remarks made over recorded lines.

Police Reports and Discovery

We will do our best to provide you with copies of everything we receive on your case. Most information will be emailed, so please keep your email address up to date.

Changes in Contact Information

If you move or change numbers during the case, please let us know. It is difficult to help if we are unable to reach you, and helping you is why we are here.

Court Appearances

Cases do not get resolved as quickly as they do on television. Expect there to be several hearings in your case and it may be necessary for you to attend one or more of them. If a hearing is set, you will receive notice of the date and time of each hearing.

Billing and Collections

We understand that this investment was a huge decision for you. As we focus on providing the best representation, we will need for you to stay on schedule with any payment arrangements agreed to at the time of your initial consultation.

Again, thank you for your trust in us. We look forward to getting a fantastic outcome on your case.

Target Market(s)

Criminal defense clients and their families

Industry/Entity Type

Legal

Font styles to use
Serif

Requirements
Must have
• Must incorporate all of the rules we email out. Would like diagrams, images or pictures
Nice to have
• We attached a Welcome brochure. Not sure I want it to look super similar, hence the request for infographic.

```html
<!DOCTYPE html>
<html lang="en">
<head>
<meta charset="UTF-8">
<title>Veritas Defense Group – A Few Quick Rules</title>
<link href="https://fonts.googleapis.com/css2?family=Poppins:wght@400;600;700&display=swap" rel="stylesheet">
<style>
  :root{
    --blue:#0b56b8;
    --blue-light:#1465c9;
    --blue-dark:#0a3f95;
    --navy:#1c2230;
    --sky:#1b8fd8;
    --grey:#ececec;
    --grey-soft:#f6f6f6;
    --ink:#1d1d1f;
    --white:#ffffff;
  }
  *{margin:0;padding:0;box-sizing:border-box}
  html,body{width:675px;height:1200px;overflow:hidden;background:var(--white)}
  body{font-family:'Poppins',sans-serif;color:var(--ink);position:relative}

  .header{position:absolute;left:0;top:0;width:675px;height:140px;text-align:center}
  .brand{position:absolute;top:20px;left:0;width:100%;display:flex;justify-content:center;align-items:center;gap:9px}
  .brand-mark{width:22px;height:22px;background:var(--sky)}
  .brand-name{font-weight:700;font-size:26px;letter-spacing:.3px;color:var(--navy);line-height:1}
  .pill{display:inline-block;background:var(--blue);color:var(--white);font-weight:700;border-radius:20px}
  .header .pill{position:absolute;top:60px;left:242px;width:170px;height:28px;line-height:28px;font-size:16px}
  .intro{position:absolute;top:92px;left:40px;width:595px;font-size:14.5px;line-height:17px;color:var(--ink)}

  .rule{position:absolute;left:0;width:675px;height:129px;overflow:hidden}
  .rule--blue{background:var(--blue)}
  .rule--grey{background:var(--grey-soft)}
  .rule--blue::before{content:"";position:absolute;inset:0;background:var(--blue-light);
    clip-path:polygon(268px 0,578px 0,527px 100%,217px 100%)}
  .rule--blue::after{content:"";position:absolute;inset:0;background:var(--blue-dark);opacity:.35;
    clip-path:polygon(578px 0,675px 0,675px 100%,527px 100%)}
  .rule--grey::before{content:"";position:absolute;inset:0;background:var(--grey);
    clip-path:polygon(153px 0,462px 0,412px 100%,102px 100%)}

  .photo{position:absolute;top:0;height:129px;width:200px;z-index:1}
  .rule--blue .photo{left:0;-webkit-mask-image:linear-gradient(90deg,#000 60%,transparent);mask-image:linear-gradient(90deg,#000 60%,transparent)}
  .rule--grey .photo{right:0;-webkit-mask-image:linear-gradient(270deg,#000 65%,transparent);mask-image:linear-gradient(270deg,#000 65%,transparent)}
  .photo--handshake{background:linear-gradient(135deg,#e8edf4,#8fa3c2 60%,#2f4f8a)}
  .photo--meeting{background:linear-gradient(160deg,#9fb27a,#dfe4ea 45%,#c9d3e3)}
  .photo--cell{background:linear-gradient(120deg,#3a3a3a,#5c5c5c 50%,#2b2b2b)}
  .photo--envelope{background:linear-gradient(135deg,#e2cfa6,#c4a266 55%,#6b5233)}
  .photo--phone{background:linear-gradient(135deg,#2b2b2b,#b8b8b8 45%,#3a3a3a)}
  .photo--courthouse{background:linear-gradient(180deg,#5f97d8,#dfe8f2 55%,#f4f4f4)}
  .photo--desk{background:linear-gradient(135deg,#2f3542,#e4e8ef 50%,#8aa0c9)}

  .rule-text{position:absolute;z-index:2;width:421px}
  .rule--blue .rule-text{left:209px;color:var(--white)}
  .rule--grey .rule-text{left:50px;color:var(--ink)}
  .rule-title{font-weight:700;font-size:16.5px;line-height:20px;margin-bottom:3px}
  .rule--grey .rule-title{color:var(--ink)}
  .rule-body{font-size:11.6px;line-height:13.5px;text-align:justify;hyphens:auto}

  .footer{position:absolute;left:0;top:1040px;width:675px;height:160px;text-align:center}
  .thanks{position:absolute;top:10px;width:100%;color:var(--sky);font-size:15px;line-height:17px}
  .footer .pill{position:absolute;top:57px;left:243px;width:184px;height:27px;line-height:27px;font-size:16px}
  .phones{position:absolute;top:92px;left:48px;width:577px;display:flex;justify-content:space-between;font-size:14.5px}
  .phones b{font-weight:700}
  .links{position:absolute;top:113px;left:50px;width:575px;display:flex;justify-content:space-between;text-align:left}
  .link{display:flex;align-items:center;gap:14px;font-size:12px;line-height:13px}
  .link b{display:block;font-weight:700}
  .link svg{flex:none}
</style>
</head>
<body>
  <header class="header">
    <div class="brand"><span class="brand-mark"></span><span class="brand-name">VERITAS DEFENSE GROUP</span></div>
    <span class="pill">A Few Quick Rules</span>
    <p class="intro">We are here to help each step of the way. While questions are never discouraged, this letter will answer some of the most common ones we get asked.</p>
  </header>

  <section class="rule rule--blue" style="top:140px">
    <div class="photo photo--handshake" role="img" aria-label="Photo of a lawyer shaking hands with a client"></div>
    <div class="rule-text" style="top:18px">
      <h2 class="rule-title">Communication</h2>
      <p class="rule-body">As a client, you should always be in the loop. While we will try to respond to questions as quickly as possible, sometimes we are unable to respond right away. Do not worry - we promise to get back to you soon. Some questions might take some time to research, and a correct answer is better than a quick one.</p>
    </div>
  </section>

  <section class="rule rule--grey" style="top:268px">
    <div class="photo photo--meeting" role="img" aria-label="Photo of a smiling attorney meeting clients at a table"></div>
    <div class="rule-text" style="top:16px">
      <h2 class="rule-title">Appointments</h2>
      <p class="rule-body">One of the benefits of having an attorney is the ability to discuss your case outside of court, minus the stress and headaches. If you need an appointment, please contact the office. Appointments must be scheduled in advance. We do not want you to make a special trip to the office only to learn that we are in court or otherwise unavailable.</p>
    </div>
  </section>

  <section class="rule rule--blue" style="top:397px">
    <div class="photo photo--cell" role="img" aria-label="Photo of a man sitting in a jail cell"></div>
    <div class="rule-text" style="top:11px">
      <h2 class="rule-title">Jail Visits</h2>
      <p class="rule-body">If your family member is currently in jail, we take that very seriously. We will visit your loved one and introduce ourselves. While the case is ongoing, we ask that a family member be designated a “contact” person so that messages can be relayed quickly. Never discuss the facts of the case over the phone with someone who is in jail. Jail calls are recorded and we have seen too many cases go south based on remarks made over recorded lines.</p>
    </div>
  </section>

  <section class="rule rule--grey" style="top:525px">
    <div class="photo photo--envelope" role="img" aria-label="Photo of a hand holding a confidential case envelope"></div>
    <div class="rule-text" style="top:29px">
      <h2 class="rule-title">Police Reports and Discovery</h2>
      <p class="rule-body">We will do our best to provide you with copies of everything we receive on your case. Most information will be emailed, so please keep your email address up to date.</p>
    </div>
  </section>

  <section class="rule rule--blue" style="top:654px">
    <div class="photo photo--phone" role="img" aria-label="Photo of a vintage rotary telephone"></div>
    <div class="rule-text" style="top:29px">
      <h2 class="rule-title">Changes in Contact Information</h2>
      <p class="rule-body">If you move or change numbers during the case, please let us know. It is difficult to help if we are unable to reach you, and helping you is why we are here.</p>
    </div>
  </section>

  <section class="rule rule--grey" style="top:783px">
    <div class="photo photo--courthouse" role="img" aria-label="Photo of a columned courthouse"></div>
    <div class="rule-text" style="top:23px">
      <h2 class="rule-title">Court Appearances</h2>
      <p class="rule-body">Cases do not get resolved as quickly as they do on television. Expect there to be several hearings in your case and it may be necessary for you to attend one or more of them. If a hearing is set, you will receive notice of the date and time of each hearing.</p>
    </div>
  </section>

  <section class="rule rule--blue" style="top:911px">
    <div class="photo photo--desk" role="img" aria-label="Photo of hands using a laptop and calculator over billing papers"></div>
    <div class="rule-text" style="top:23px">
      <h2 class="rule-title">Billing and Collections</h2>
      <p class="rule-body">We understand that this investment was a huge decision for you. As we focus on providing the best representation, we will need for you to stay on schedule with any payment arrangements agreed to at the time of your initial consultation.</p>
    </div>
  </section>

  <footer class="footer">
    <p class="thanks">Again, thank you for your trust in us.<br>We look forward to getting a fantastic outcome on your case.</p>
    <span class="pill">Calls answered 24/7</span>
    <div class="phones">
      <span>Toll free <b>(888) 555-0142</b></span>
      <span>LA area <b>(213) 555-0142</b></span>
      <span>Inland <b>(909) 555-0168</b></span>
    </div>
    <div class="links">
      <div class="link">
        <svg width="30" height="30" viewBox="0 0 30 30" aria-hidden="true">
          <circle cx="15" cy="15" r="13.5" fill="none" stroke="#0b56b8" stroke-width="2.5"/>
          <ellipse cx="15" cy="15" rx="6" ry="13.5" fill="none" stroke="#0b56b8" stroke-width="2"/>
          <line x1="15" y1="1.5" x2="15" y2="28.5" stroke="#0b56b8" stroke-width="2"/>
          <line x1="1.5" y1="15" x2="28.5" y2="15" stroke="#0b56b8" stroke-width="2"/>
          <path d="M4 8.5h22M4 21.5h22" stroke="#0b56b8" stroke-width="2"/>
        </svg>
        <span><b>Visit us online</b>www.veritasdefensegroup.com</span>
      </div>
      <div class="link">
        <svg width="30" height="20" viewBox="0 0 30 20" aria-hidden="true">
          <rect x="0" y="0" width="30" height="20" fill="#0b56b8"/>
          <path d="M1 1l14 11L29 1M1 19l10-9M29 19l-10-9" fill="none" stroke="#fff" stroke-width="1.6"/>
        </svg>
        <span><b>Email us</b>info@veritasdefensegroup.com</span>
      </div>
    </div>
  </footer>
</body>
</html>
```